My project benefits Military, First Responders, Police, Fire, and Educators.

Contact Information for Business Card

2 Sided appointment card. Visual side will have my head shot with "Summit Venture" in a bold graffic/text. I am picturing maybe the headshot applied to a filter that has a matrix effect where the picture is made up of data/numbers flowing vertically through the photo. I am of course open to other concepts as well. Side two will have contact info presented in an attractive visual complimenting the front.

```html
<!DOCTYPE html>
<html lang="en">
<head>
<meta charset="utf-8">
<title>Summit Venture – Appointment Card</title>
<link href="https://fonts.googleapis.com/css2?family=PT+Sans:ital,wght@0,400;0,700;1,700&display=swap" rel="stylesheet">
<style>
  :root {
    --backdrop: #1a1a1a;
    --card: #ffffff;
    --brand-red: #c41a1c;
    --ink: #2b2b2b;
    --ink-soft: #444444;
    --rule: #9a9a9a;
  }
  html, body {
    margin: 0;
    padding: 0;
    width: 1200px;
    height: 900px;
    overflow: hidden;
    background: var(--backdrop);
    font-family: "PT Sans", Arial, sans-serif;
  }
  .stage {
    position: relative;
    width: 1200px;
    height: 900px;
  }
  .card {
    position: absolute;
    top: 306px;
    width: 440px;
    height: 272px;
    background: var(--card);
    border-radius: 10px;
    overflow: hidden;
  }
  .card--front { left: 149px; }
  .card--back { left: 608px; }

  /* Front */
  .headshot {
    position: absolute;
    left: 0;
    top: 14px;
    width: 246px;
    height: 258px;
    background: linear-gradient(180deg, #b58a6c 0%, #a87a5d 40%, #2a3350 62%, #1c2438 100%);
    border-top-right-radius: 110px 90px;
  }
  .wordmark {
    position: absolute;
    right: 36px;
    top: 40px;
    margin: 0;
    color: var(--brand-red);
    font-weight: 700;
    font-size: 34px;
    line-height: 38px;
    text-align: right;
    letter-spacing: 1px;
  }
  .person {
    position: absolute;
    right: 36px;
    top: 144px;
    text-align: right;
  }
  .person__name {
    margin: 0;
    color: var(--brand-red);
    font-weight: 700;
    font-size: 18px;
    line-height: 20px;
  }
  .person__role {
    margin: 0;
    color: var(--ink-soft);
    font-size: 12px;
    line-height: 14px;
  }
  .contact {
    position: absolute;
    right: 36px;
    top: 198px;
    margin: 0;
    padding: 0;
    list-style: none;
    text-align: right;
    color: var(--ink);
    font-size: 12px;
    line-height: 16px;
  }
  .contact li { display: flex; justify-content: flex-end; align-items: center; gap: 5px; }
  .contact svg { width: 9px; height: 9px; fill: var(--brand-red); }

  /* Back */
  .back-header {
    height: 91px;
    background: var(--brand-red);
    display: flex;
    align-items: center;
    justify-content: center;
  }
  .back-header .wordmark-light {
    margin: 0;
    color: #ffffff;
    font-weight: 700;
    font-size: 28px;
    line-height: 30px;
    text-align: center;
    letter-spacing: 1px;
  }
  .step-mark {
    position: absolute;
    left: 33px;
    top: 100px;
    width: 46px;
    height: 82px;
    background: var(--brand-red);
    border-radius: 20px 20px 18px 18px;
  }
  .next-label {
    position: absolute;
    left: 83px;
    top: 126px;
    margin: 0;
    color: var(--ink);
    font-size: 14px;
  }
  .next-title {
    position: absolute;
    left: 83px;
    top: 148px;
    margin: 0;
    color: var(--brand-red);
    font-weight: 400;
    font-size: 25px;
  }
  .write-line {
    position: absolute;
    left: 29px;
    width: 384px;
    height: 1px;
    background: var(--rule);
  }
  .write-line--one { top: 206px; }
  .write-line--two { top: 234px; }
  .notice {
    position: absolute;
    left: 0;
    right: 0;
    top: 243px;
    margin: 0;
    text-align: center;
    color: #111111;
    font-style: italic;
    font-weight: 700;
    font-size: 10.5px;
  }
</style>
</head>
<body>
<main class="stage">
  <section class="card card--front" aria-label="Front of appointment card">
    <div class="headshot" role="img" aria-label="Headshot of the managing director in a navy suit and tie"></div>
    <h1 class="wordmark">SUMMIT<br>VENTURE</h1>
    <div class="person">
      <p class="person__name">Daniel Harper</p>
      <p class="person__role">Managing Director</p>
    </div>
    <ul class="contact">
      <li>555-204-7731
        <svg viewBox="0 0 10 10" aria-hidden="true"><path d="M1 3 Q1 1 3 1 L7 1 Q9 1 9 3 L9 4 L7 4 L7 3 L3 3 L3 4 L1 4 Z M2 5 L8 5 L9 9 L1 9 Z"/></svg>
      </li>
      <li>hello@summitventure.com
        <svg viewBox="0 0 10 10" aria-hidden="true"><path d="M0 2 H10 V8 H0 Z" /><path d="M0 2 L5 6 L10 2" stroke="#fff" stroke-width="1" fill="none"/></svg>
      </li>
      <li>www.summitventure.com
        <svg viewBox="0 0 10 10" aria-hidden="true"><path d="M2 6 L4 8 M6 2 L8 4 M3 7 L7 3" stroke="#c41a1c" stroke-width="1.6" fill="none" stroke-linecap="round"/></svg>
      </li>
    </ul>
  </section>

  <section class="card card--back" aria-label="Back of appointment card">
    <header class="back-header">
      <h2 class="wordmark-light">SUMMIT<br>VENTURE</h2>
    </header>
    <div class="step-mark" role="img" aria-label="Footprint illustration"></div>
    <p class="next-label">Your Next</p>
    <h3 class="next-title">Appointment :</h3>
    <div class="write-line write-line--one"></div>
    <div class="write-line write-line--two"></div>
    <p class="notice">Please give 24 hours notice if you need to reschedule your appointment</p>
  </section>
</main>
</body>
</html>
```